executive development which breaks down traditional practices and thought processes

4 or 5 page website. Home page idea is fixed but needs creative execution to work {see attachment}, branding, as in corporate identity is in place and ready to go, (see attachment). Site needs to reflect the the market and typical participant, which are very high achievers up to and including Board Level Members in 'world leading company's'.

What we do is different, we are often copied, but without the success.

We require simple, slick impact, we have powerful messages that need to be supported by exquisite, simplistic design. We know we are the best out there and have kept our heads under water, but now is the time to start our expansion process.

We have copywriters briefed, and are liking what we read, so time to engage with designers who might like to 'wow' us, as well as our existing and potential clients.

Pages to include a standard landing/home page, about us, methodology, testimonials/awards and let's talk pages. Our philosophy is: opening minds to new ways of thinking, being, working and acting; to challenge long held business, management and leadership biases.

Our experiential learning technique is branded 'Quillmark' where we take people out of their comfort zone or into new & very different environments; to experience the way methodology and leadership techniques from uncomfortable encounters can be beneficial in big business strategic decision making, being more innovative and solving leadership & managerial challenges with new eyes (or a new perspective).

We will need to include video clips for awards we have won and testimonials from participants and company's alike. We work across the globe, the site needs to reflect this, without us looking like a huge corporate company, which we are not. We are small but pack a powerful punch, and that's the way we like it. Our clients don't see us as consultants or suppliers, more as the missing cog or the oil in the machine to get their executives to engage and deliver unorthodox thought processes which keep them at the forefront of their industries.

Both the copywriters and ourselves see typography being a crucial element to the impact of the site, so those designers with a passion in this area may well find our preference.

We are ready to go, good luck.

sorry guys missing the brief by a long way, we always said we were not looking for an off the shelf solution/concept which could be created on any 'zip merlo' like ortal and to be honest that's all we have received

Reason: designs miss the brief

Reason: We are not getting the desired simplistic landing page required.

```html
<!DOCTYPE html>
<html lang="en">
<head>
<meta charset="utf-8">
<title>Ardent — Executive Development</title>
<link href="https://fonts.googleapis.com/css2?family=Lato:wght@400;700&family=Montserrat:wght@300&family=Varela+Round&display=swap" rel="stylesheet">
<style>
  :root {
    --brand-green: #3de000;
    --brand-violet: #4a00e6;
    --text-dark: #333333;
    --text-mid: #555555;
    --card-top: #ffffff;
    --card-bottom: #e6e6e6;
    --footer-bg: #e9e9e9;
    --white: #ffffff;
    --sky: #c3e2ec;
    --water-light: #5fb3d6;
    --water-deep: #1f7fb3;
    --skin: #b0704a;
  }
  * { box-sizing: border-box; margin: 0; padding: 0; }
  html, body { width: 1200px; height: 750px; overflow: hidden; }
  body { font-family: 'Lato', sans-serif; background: var(--footer-bg); position: relative; }

  .hero {
    position: absolute; left: 0; top: 0; width: 1200px; height: 647px;
    background:
      radial-gradient(ellipse 520px 180px at 600px 340px, rgba(176,112,74,0.55), rgba(176,112,74,0) 70%),
      linear-gradient(180deg, var(--sky) 0%, #8cc6dc 30%, var(--water-light) 55%, var(--water-deep) 85%, #2d8cc0 100%);
  }

  .brand-plate {
    position: absolute; left: 132px; top: 19px; width: 253px; height: 96px;
    background: linear-gradient(180deg, var(--card-top), var(--card-bottom));
    border-radius: 4px; box-shadow: 0 4px 6px rgba(0,0,0,0.35);
  }
  .brand-plate .brand-name {
    position: absolute; left: 24px; top: 4px;
    font-family: 'Varela Round', sans-serif; font-size: 62px; color: var(--brand-green); line-height: 1;
  }
  .brand-plate .brand-tagline {
    position: absolute; right: 22px; top: 70px; font-size: 12px; color: var(--text-mid);
  }

  .main-nav { position: absolute; top: 56px; left: 549px; display: flex; }
  .main-nav a {
    color: var(--white); font-weight: 700; font-size: 15px; text-decoration: none;
    height: 32px; line-height: 30px; padding: 0 15px; border: 1px solid transparent; border-radius: 3px;
  }
  .main-nav a.active { border-color: var(--brand-violet); }
  .main-nav a + a { margin-left: 7px; }
  .main-nav a:nth-child(3) { margin-left: 11px; line-height: 26px; }
  .main-nav a:nth-child(4) { margin-left: 19px; }
  .main-nav a:nth-child(5) { margin-left: 13px; }

  .hero-title {
    position: absolute; top: 252px; left: 0; width: 1200px; text-align: center;
    font-family: 'Varela Round', sans-serif; font-size: 45px; color: var(--brand-green); font-weight: 400;
    -webkit-text-stroke: 0.6px var(--brand-green);
  }
  .hero-lede {
    position: absolute; top: 315px; left: 0; width: 1200px; text-align: center;
    font-family: 'Montserrat', sans-serif; font-weight: 300; font-size: 19px; line-height: 24px; color: var(--white);
  }
  .hero-cta {
    position: absolute; left: 536px; top: 381px; width: 126px; height: 36px;
    border: 1px solid var(--white); border-radius: 3px; color: var(--white);
    font-weight: 700; font-size: 17px; line-height: 34px; text-align: center;
  }
  .slide-arrow { position: absolute; top: 304px; }
  .slide-arrow.prev { left: 85px; }
  .slide-arrow.next { left: 1087px; }

  .step-card {
    position: absolute; top: 498px; width: 263px; height: 103px;
    background: linear-gradient(180deg, var(--card-top), var(--card-bottom));
    border-radius: 3px; box-shadow: 0 3px 5px rgba(0,0,0,0.35);
    display: flex; align-items: center; padding: 0 14px 0 43px;
    font-size: 14px; line-height: 20px; color: var(--text-dark);
  }
  .step-number {
    position: absolute; left: -27px; top: 22px; width: 58px; height: 58px; border-radius: 50%;
    background: var(--brand-green); border-right: 2px solid #2a6fc0;
    color: var(--brand-violet); font-family: 'Varela Round', sans-serif; font-size: 30px;
    display: flex; align-items: center; justify-content: center;
  }
  .step-one { left: 157px; }
  .step-two { left: 482px; }
  .step-three { left: 806px; }
  .step-chevron { position: absolute; top: 535px; }
  .step-chevron.prev { left: 94px; }
  .step-chevron.next { left: 1088px; }

  .site-footer { position: absolute; left: 0; top: 647px; width: 1200px; height: 103px; background: var(--footer-bg); }
  .footer-nav { position: absolute; left: 143px; top: 12px; font-size: 13px; color: var(--text-dark); white-space: nowrap; }
  .footer-nav span { position: absolute; top: 0; }
  .footer-contact { position: absolute; font-size: 13px; line-height: 20px; color: var(--text-dark); }
  .footer-contact svg { position: absolute; left: -20px; }
  .footer-brand {
    position: absolute; left: 627px; top: 10px; width: 116px; text-align: center;
    font-family: 'Varela Round', sans-serif; color: var(--brand-green); font-size: 30px; line-height: 30px;
  }
  .footer-brand small { display: block; font-family: 'Lato', sans-serif; font-size: 8px; line-height: 10px; color: var(--text-mid); text-align: right; }
  .social-links { position: absolute; left: 642px; top: 75px; display: flex; gap: 10px; }
  .social-links span { width: 14px; height: 14px; border-radius: 50%; background: #444444; display: block; }
  .subscribe { position: absolute; left: 802px; top: 18px; display: flex; }
  .subscribe .email-field {
    width: 174px; height: 33px; background: var(--white); border: 1px solid #cccccc; border-right: none;
    border-radius: 2px 0 0 2px; font-size: 12px; font-style: italic; color: #777777;
    display: flex; align-items: center; gap: 8px; padding-left: 10px;
  }
  .subscribe .subscribe-button {
    width: 92px; height: 33px; background: var(--brand-violet); color: var(--white);
    font-weight: 700; font-size: 14px; line-height: 33px; text-align: center;
  }
  .copyright { position: absolute; left: 805px; top: 72px; font-size: 13px; color: var(--text-dark); }
</style>
</head>
<body>

<section class="hero" role="img" aria-label="Photograph of a swimmer doing butterfly stroke through splashing blue pool water"></section>

<header>
  <div class="brand-plate">
    <span class="brand-name">ardent</span>
    <span class="brand-tagline">Executive development</span>
  </div>
  <nav class="main-nav">
    <a class="active" href="#">Home</a>
    <a href="#">About Us</a>
    <a href="#">Methodology</a>
    <a href="#">Testimonials</a>
    <a href="#">Let's Talk</a>
  </nav>
</header>

<h1 class="hero-title">Executive Development</h1>
<p class="hero-lede">Being more innovative and solving leadership &amp;<br>managerial challenges with new eyes</p>
<div class="hero-cta">LEARN MORE</div>

<svg class="slide-arrow prev" width="28" height="54" viewBox="0 0 28 54"><polyline points="27,1 1,27 27,53" fill="none" stroke="#fff" stroke-width="2"/></svg>
<svg class="slide-arrow next" width="28" height="54" viewBox="0 0 28 54"><polyline points="1,1 27,27 1,53" fill="none" stroke="#fff" stroke-width="2"/></svg>

<div class="step-card step-one"><span class="step-number">1</span>The act or an instance of looking for or seeking; search: a quest for diamonds.</div>
<div class="step-card step-two"><span class="step-number">2</span>An expedition by aknightor company of knights to accomplish some prescribed task, such as finding the Holy Grail</div>
<div class="step-card step-three"><span class="step-number">3</span>The object of a search; goal or target: my quest is the treasure of the king.</div>

<svg class="step-chevron prev" width="14" height="28" viewBox="0 0 14 28"><polyline points="12,2 3,14 12,26" fill="none" stroke="#cfd6da" stroke-width="4"/></svg>
<svg class="step-chevron next" width="14" height="28" viewBox="0 0 14 28"><polyline points="2,2 11,14 2,26" fill="none" stroke="#cfd6da" stroke-width="4"/></svg>

<footer class="site-footer">
  <div class="footer-nav">
    <span style="left:0">Home</span>
    <span style="left:50px">|</span>
    <span style="left:71px">About</span>
    <span style="left:118px">|</span>
    <span style="left:135px">Methodology</span>
    <span style="left:226px">|</span>
    <span style="left:252px">Testimonials</span>
    <span style="left:341px">|</span>
    <span style="left:367px">Let's Talk</span>
  </div>

  <div class="footer-contact" style="left:160px; top:48px;">
    <svg width="10" height="14" viewBox="0 0 10 14" style="top:3px; left:-20px"><path d="M5 0a5 5 0 0 0-5 5c0 4 5 9 5 9s5-5 5-9a5 5 0 0 0-5-5zm0 7a2 2 0 1 1 0-4 2 2 0 0 1 0 4z" fill="#666"/></svg>
    Loream ipsum, Dollar smit,<br>Gunhaberg - 0123989.
  </div>
  <div class="footer-contact" style="left:367px; top:46px;">
    <svg width="11" height="11" viewBox="0 0 11 11" style="top:5px; left:-26px"><path d="M2 0l2 2-1 2c1 2 2 3 4 4l2-1 2 2-2 2C4 11 0 7 0 2z" fill="#666"/></svg>
    123-456-7890
  </div>
  <div class="footer-contact" style="left:365px; top:67px;">
    <svg width="11" height="8" viewBox="0 0 11 8" style="top:7px; left:-22px"><rect width="11" height="8" fill="#666"/><polyline points="0,0 5.5,4.5 11,0" fill="none" stroke="#e9e9e9" stroke-width="1"/></svg>
    info@ardentexec.com
  </div>

  <div class="footer-brand">ardent<small>Executive development</small></div>
  <div class="social-links" aria-label="Social links">
    <span></span><span></span><span></span><span></span>
  </div>

  <div class="subscribe">
    <div class="email-field">
      <svg width="16" height="11" viewBox="0 0 16 11"><rect x="0.5" y="0.5" width="15" height="10" fill="none" stroke="#bbb"/><polyline points="0.5,0.5 8,6 15.5,0.5" fill="none" stroke="#bbb"/></svg>
      your e-mail address
    </div>
    <div class="subscribe-button">SUBSCRIBE</div>
  </div>
  <p class="copyright">Copyright © 2014 Ardent. All Right Reserved</p>
</footer>

</body>
</html>
```